Automotive component supplier needs a business card design

We need a business card design for our company called Velmar Global Components Ltd based in the UK. We are a supplier of interior and exterior components to premium car manufacturers such as Corvane Hale, Durrant Fyfe, Maxtorn and Valdessimo. We would like to see a modern business card design that uses the colour blue.

Target Market(s)

Premium automotive car manufacturers.

Industry/Entity Type

Automotive

Contact Information for Business Card

Company Name : Velmar Global Components Limited
Address: 17 Tamsey Yard, Upper Drisk, Warwick, CV31 8RJ, United Kingdom
Web Address : www.velmarparts-example.co.uk

Font styles to use
Other font styles liked:
• Helvetica

Colors
3176b5
0255a3
85acd3
cfdeed
cee9f5
85cae6
34a6d7
0692cd
9bcb3c

Requirements
Must have
• Clear company logo and a mixture of blue colours.
Nice to have
• A high quality modern image.
Should not have
• Multiple colours.

```html
<!DOCTYPE html>
<html lang="en">
<head>
<meta charset="utf-8">
<title>Velmar Global Components – Business Card</title>
<link href="https://fonts.googleapis.com/css2?family=Arimo:wght@400;700&display=swap" rel="stylesheet">
<style>
  :root {
    --sky: #34a6d7;
    --cyan: #0fb2dc;
    --navy: #0255a3;
    --lime: #9bcb3c;
    --paper: #f7f8f9;
    --paper-shade: #e9ecee;
    --ink: #0692cd;
    --bg: #e4e7ea;
  }
  * { margin: 0; padding: 0; box-sizing: border-box; }
  html, body { width: 1200px; height: 1023px; overflow: hidden; }
  body {
    background: var(--bg);
    font-family: "Arimo", Helvetica, Arial, sans-serif;
    position: relative;
  }
  .card {
    position: absolute;
    width: 560px;
    height: 320px;
    border-radius: 14px;
    background: linear-gradient(135deg, #ffffff 0%, var(--paper) 55%, var(--paper-shade) 100%);
    box-shadow: 0 6px 18px rgba(0,0,0,0.18);
    overflow: hidden;
  }
  .card--front { left: 90px; top: 110px; }
  .card--back { left: 550px; top: 590px; }

  .edge-band {
    position: absolute;
    top: 0; bottom: 0;
    width: 30px;
    display: flex;
    flex-direction: column;
  }
  .edge-band--left { left: 0; }
  .edge-band--right { right: 0; }
  .edge-band span { display: block; }
  .seg-sky { background: var(--sky); }
  .seg-lime { background: var(--lime); }
  .seg-navy { background: var(--navy); }

  .front-name {
    position: absolute;
    left: 30px; right: 30px;
    top: 88px;
    text-align: center;
    color: var(--cyan);
    font-weight: 400;
  }
  .front-name .word {
    display: block;
    font-size: 92px;
    letter-spacing: 4px;
    line-height: 1;
  }
  .front-name .sub {
    display: block;
    margin-top: 12px;
    font-size: 25px;
    letter-spacing: 5px;
  }

  .accent-lines {
    position: absolute;
    left: 38px; top: 0;
    width: 10px; height: 74px;
  }
  .person {
    position: absolute;
    left: 60px; top: 30px;
  }
  .person .name { color: var(--ink); font-size: 22px; }
  .person .title { color: var(--lime); font-size: 13px; margin-top: 3px; }

  .contact {
    position: absolute;
    left: 40px; top: 170px;
    list-style: none;
    color: var(--ink);
    font-size: 13.5px;
    line-height: 1.5;
  }
  .contact li { display: flex; align-items: flex-start; gap: 8px; }
  .contact svg { width: 12px; height: 12px; margin-top: 4px; flex: none; }
  .contact .addr { display: block; }

  .back-name {
    position: absolute;
    right: 40px; top: 34px;
    text-align: right;
    color: var(--cyan);
    font-weight: 400;
  }
  .back-name .word { display: block; font-size: 40px; letter-spacing: 2px; line-height: 1; }
  .back-name .sub { display: block; font-size: 11px; letter-spacing: 2.5px; margin-top: 5px; }

  .web {
    position: absolute;
    right: 40px; bottom: 26px;
    color: var(--ink);
    font-size: 13.5px;
    display: flex; align-items: center; gap: 7px;
  }
  .web svg { width: 12px; height: 12px; }
  .corner-lines {
    position: absolute;
    right: 0; bottom: 0;
    width: 30px; height: 10px;
  }
</style>
</head>
<body>

<section class="card card--front" aria-label="Card front">
  <div class="edge-band edge-band--left">
    <span class="seg-sky" style="flex:1.1"></span>
    <span class="seg-navy" style="flex:1.1"></span>
    <span class="seg-lime" style="flex:1"></span>
    <span class="seg-sky" style="flex:0.8"></span>
  </div>
  <div class="edge-band edge-band--right">
    <span class="seg-sky" style="flex:0.8"></span>
    <span class="seg-lime" style="flex:1"></span>
    <span class="seg-navy" style="flex:1.1"></span>
    <span class="seg-sky" style="flex:1.1"></span>
  </div>
  <h1 class="front-name">
    <span class="word">VELMAR</span>
    <span class="sub">GLOBAL COMPONENTS</span>
  </h1>
</section>

<section class="card card--back" aria-label="Card back">
  <svg class="accent-lines" viewBox="0 0 10 74" aria-hidden="true">
    <rect x="0" y="0" width="4" height="74" fill="#34a6d7"/>
    <rect x="6" y="0" width="3" height="74" fill="#9bcb3c"/>
  </svg>
  <div class="person">
    <p class="name">Your Name</p>
    <p class="title">Title</p>
  </div>

  <div class="back-name">
    <span class="word">VELMAR</span>
    <span class="sub">GLOBAL COMPONENTS</span>
  </div>

  <ul class="contact">
    <li>
      <svg viewBox="0 0 12 12" aria-hidden="true"><path d="M6 0.5a4 4 0 0 0-4 4c0 3 4 7 4 7s4-4 4-7a4 4 0 0 0-4-4zm0 5.5a1.5 1.5 0 1 1 0-3 1.5 1.5 0 0 1 0 3z" fill="#9bcb3c"/></svg>
      <span class="addr">17 Tamsey Yard, Upper Drisk, Warwick,<br>CV31 8RJ, United Kingdom</span>
    </li>
    <li>
      <svg viewBox="0 0 12 12" aria-hidden="true"><circle cx="6" cy="6" r="5" fill="none" stroke="#9bcb3c" stroke-width="1.2"/><path d="M4.2 3.6l1 1-.6.7c.4.9 1.1 1.6 2 2l.7-.6 1 1-.8.8c-1.9-.3-3.8-2.2-4.1-4.1z" fill="#9bcb3c"/></svg>
      <span>(555)010-472</span>
    </li>
    <li>
      <svg viewBox="0 0 12 12" aria-hidden="true"><rect x="0.8" y="2.5" width="10.4" height="7" fill="none" stroke="#9bcb3c" stroke-width="1.1"/><path d="M0.8 2.5l5.2 4 5.2-4" fill="none" stroke="#9bcb3c" stroke-width="1.1"/></svg>
      <span>info@velmarparts-example.co.uk</span>
    </li>
  </ul>

  <p class="web">
    <span>www.velmarparts-example.co.uk</span>
    <svg viewBox="0 0 12 12" aria-hidden="true"><circle cx="6" cy="6" r="5" fill="none" stroke="#9bcb3c" stroke-width="1.1"/><ellipse cx="6" cy="6" rx="2.2" ry="5" fill="none" stroke="#9bcb3c" stroke-width="0.9"/><path d="M1 6h10" stroke="#9bcb3c" stroke-width="0.9"/></svg>
  </p>

  <svg class="corner-lines" viewBox="0 0 30 10" aria-hidden="true">
    <rect x="0" y="0" width="30" height="4" fill="#34a6d7"/>
    <rect x="0" y="6" width="30" height="3" fill="#9bcb3c"/>
  </svg>
</section>

</body>
</html>
```